out of the box Business Card Design for a Manufacturer / Distributor

We are a manufarturer and distributor of products.
the company name is VORTANI (Pic attached)

the picture is NOT a must have on the business Card.

the Business Card should look really professional and/or special, so out of the box thinking is welcome.

there should be 2 Adresses on the Business Card for Main and Branch Office.
Email Adress, homepage, Name is required
NO Phone Number

Our working field:
Private Labeling
high Quality Production
direct distribution
warehousing
trademark registration
legal support

Main Office:
Kornblumenweg 14
08352 Halvenberg
Germany

Branch Office:
Daska Lane
Zarvanpur
Pakistan

Names:
Lukas Feldhaus (Owner)
Imran Qureshi (Owner)

Email:
lukas@vortani-example.com
imran@vortani-example.com

homepage:
vortani-example.com

Industry/Entity Type

Manufacturer Distributer

Contact Information for Business Card

Vortani

Requirements
Must have
• Names, both office Adresses, email, homepage
Should not have
• Phone Number

```html
<!DOCTYPE html>
<html lang="en">
<head>
<meta charset="utf-8">
<title>VORTANI – Business Card</title>
<link rel="stylesheet" href="https://fonts.googleapis.com/css2?family=Montserrat:wght@300;400;700&display=swap">
<style>
  :root {
    --canvas: #e9e7e4;
    --card-dark: #3b3b3d;
    --card-light: #f5f5f4;
    --ink: #2e2e30;
    --ink-soft: #4a4a4c;
    --white: #ffffff;
  }
  * { box-sizing: border-box; margin: 0; padding: 0; }
  html, body {
    width: 1200px; height: 900px; overflow: hidden;
    background: var(--canvas);
    font-family: "Montserrat", Arial, sans-serif;
    color: var(--ink);
  }
  .sheet {
    width: 1200px; height: 900px;
    display: flex; flex-direction: column;
    align-items: center; justify-content: center; gap: 44px;
  }
  .card {
    width: 640px; height: 376px; position: relative;
    box-shadow: 0 6px 18px rgba(0,0,0,.14);
  }
  /* Front */
  .card-front { background: var(--card-dark); }
  .front-wordmark {
    position: absolute; left: 210px; top: 140px;
    font-size: 74px; font-weight: 400; letter-spacing: 3px;
    color: var(--white);
  }
  /* Back */
  .card-back { background: var(--card-light); }
  .back-wordmark {
    position: absolute; left: 48px; top: 112px;
    font-size: 26px; font-weight: 400; letter-spacing: 1px;
    color: var(--ink);
  }
  .people { position: absolute; left: 48px; top: 170px; }
  .person { margin-bottom: 10px; }
  .person-name { font-size: 19px; font-weight: 300; line-height: 1.1; }
  .person-name strong { font-weight: 700; }
  .person-role { font-size: 12px; font-weight: 400; color: var(--ink-soft); }
  .contacts { position: absolute; left: 48px; top: 268px; list-style: none; }
  .contact {
    display: flex; align-items: center; gap: 10px;
    font-size: 14.5px; font-weight: 700; margin-bottom: 5px;
  }
  .contact.web { font-weight: 300; }
  .contact.web strong { font-weight: 700; }
  .icon-box {
    width: 18px; height: 18px; background: var(--ink); border-radius: 3px;
    display: inline-flex; align-items: center; justify-content: center; flex: none;
  }
  .offices { position: absolute; left: 380px; top: 60px; list-style: none; }
  .office { display: flex; gap: 10px; margin-bottom: 26px; }
  .office .icon-box { margin-top: 4px; }
  .office-title { font-size: 20px; font-weight: 700; line-height: 1.1; }
  .office-lines { font-size: 15px; font-weight: 400; line-height: 1.15; color: var(--ink-soft); }
</style>
</head>
<body>
<main class="sheet">
  <section class="card card-front" aria-label="Card front">
    <div class="front-wordmark">VORTANI</div>
  </section>

  <section class="card card-back" aria-label="Card back">
    <div class="back-wordmark">VORTANI</div>

    <div class="people">
      <div class="person">
        <p class="person-name"><strong>Lukas</strong> Feldhaus</p>
        <p class="person-role">Chief Executive Office</p>
      </div>
      <div class="person">
        <p class="person-name"><strong>Imran</strong> Qureshi</p>
        <p class="person-role">Chief Executive Office</p>
      </div>
    </div>

    <ul class="contacts">
      <li class="contact">
        <span class="icon-box"><svg width="11" height="8" viewBox="0 0 11 8"><rect x=".5" y=".5" width="10" height="7" fill="none" stroke="#fff"/><path d="M.5 .5 5.5 4.5 10.5 .5" fill="none" stroke="#fff"/></svg></span>
        lukas@vortani-example.com
      </li>
      <li class="contact">
        <span class="icon-box"><svg width="11" height="8" viewBox="0 0 11 8"><rect x=".5" y=".5" width="10" height="7" fill="none" stroke="#fff"/><path d="M.5 .5 5.5 4.5 10.5 .5" fill="none" stroke="#fff"/></svg></span>
        imran@vortani-example.com
      </li>
      <li class="contact web">
        <span class="icon-box"><svg width="11" height="11" viewBox="0 0 11 11"><circle cx="5.5" cy="5.5" r="4.8" fill="none" stroke="#fff"/><ellipse cx="5.5" cy="5.5" rx="2" ry="4.8" fill="none" stroke="#fff"/><path d="M.7 5.5h9.6" stroke="#fff"/></svg></span>
        <span>www.<strong>vortani-example</strong>.com</span>
      </li>
    </ul>

    <ul class="offices">
      <li class="office">
        <span class="icon-box"><svg width="9" height="12" viewBox="0 0 9 12"><path d="M4.5 11.5C1.5 7.5.5 6 .5 4.5a4 4 0 0 1 8 0c0 1.5-1 3-4 7z" fill="#fff"/><circle cx="4.5" cy="4.5" r="1.5" fill="#2e2e30"/></svg></span>
        <div>
          <p class="office-title">Main Office</p>
          <p class="office-lines">Kornblumenweg 14<br>08352 Halvenberg<br>Germany</p>
        </div>
      </li>
      <li class="office">
        <span class="icon-box"><svg width="9" height="12" viewBox="0 0 9 12"><path d="M4.5 11.5C1.5 7.5.5 6 .5 4.5a4 4 0 0 1 8 0c0 1.5-1 3-4 7z" fill="#fff"/><circle cx="4.5" cy="4.5" r="1.5" fill="#2e2e30"/></svg></span>
        <div>
          <p class="office-title">Main Office</p>
          <p class="office-lines">Daska Lane<br>Zarvanpur<br>Pakistan</p>
        </div>
      </li>
    </ul>
  </section>
</main>
</body>
</html>
```